PREMIUM AGENCY High End Business Card - A+++ Designers Wanted

** DO NOT ATTEMPT TO CONTACT ME THROUGH SEARCHING ON ZINTREL OR EMAILING ME THROUGH MY WEBSITE **

I need a fresh, contemporary business card designed using the logo attached (BRONSALK)

I have attached the font for BRONSALK

It must have a premium look and feel. The business card size must be STANDARD size.

You can submit either/both VERTICAL or HORIZONTAL designs.

FRONT: It must have the following sample information on

Paul Ardley
Director Operations
Mobile +61 452 118 906
Email paulardley@bronsalk.com
www.bronsalk.com

The REAR of the business card must have the words

CREATE INSPIRE TOMORROW

as part of the design, in the same font (NEXA) attached.

The words do not need to be in capitals, or on the same line, please design this as you see it best working.

ADDITIONAL INFORMATION
======================

The BRONSALK logo must be on the front of the card

I want Ultraviolet printing on the final design, to enhance either the NAME of the person OR the BRONSALK logo OR the words on the back of the card.

Target Market(s)

Agency, Advertising Agency, Creative, Designers

Industry/Entity Type

Media

Contact Information for Business Card

Design Agency, Contemporary, Premium look and feel, High Quality

Font styles to use
Serif
Sans Serif
Other font styles liked:
• ATTACHED TO PROJECT

Requirements
Must have
• BLACK & WHITE as the primary design, and if you feel there can be a highlighted colour, then this can be used.
• The Logo ICON attached is blue, this colour must not be changed.
• I have attached the partner brand BRONSALK MEDIA incase you need to manipulate the original files.
• ** DO NOT ATTEMPT TO CONTACT ME THROUGH SEARCHING ON ZINTREL OR EMAILING ME THROUGH MY WEBSITE **
Nice to have
• Must be Premium. I have attached some sample designs, that I like that would be a good inspiration for where this can be taken.
• My favourite design is is the KESTRAVUE2-BUSINESSCARD-TEMPLATE
Should not have
• No funny or silly standard / off the shelf designs

```html
<!DOCTYPE html>
<html lang="en">
<head>
<meta charset="utf-8">
<title>Bronsalk Media – Business Card</title>
<link href="https://fonts.googleapis.com/css2?family=Montserrat:wght@300;400;700;800&display=swap" rel="stylesheet">
<style>
  :root {
    --brand-blue: #22a7e0;
    --ink: #1c1c1c;
    --muted: #444444;
    --paper: #ffffff;
    --backdrop: #e9e7e3;
    --rule: #9a9a9a;
  }
  * { box-sizing: border-box; margin: 0; padding: 0; }
  html, body { width: 1200px; height: 947px; overflow: hidden; }
  body {
    background: var(--backdrop);
    font-family: "Montserrat", Arial, sans-serif;
    color: var(--ink);
    position: relative;
  }
  .card {
    position: absolute;
    width: 525px;
    height: 300px;
    top: 324px;
    box-shadow: 0 6px 18px rgba(0,0,0,0.18);
    overflow: hidden;
  }
  /* Front */
  .card-front {
    left: 50px;
    background: var(--paper);
    border-top: 5px solid var(--brand-blue);
    border-bottom: 8px solid var(--brand-blue);
  }
  .brand {
    position: absolute;
    top: 62px;
    left: 0;
    width: 100%;
    display: flex;
    justify-content: center;
    align-items: center;
    gap: 14px;
  }
  .brand-dot {
    width: 26px; height: 26px;
    border-radius: 50%;
    background: var(--brand-blue);
  }
  .brand-name {
    font-weight: 700;
    font-size: 30px;
    letter-spacing: 4px;
    color: var(--ink);
  }
  .holder {
    position: absolute;
    left: 42px;
    top: 178px;
    width: 170px;
  }
  .holder-name {
    font-weight: 800;
    font-size: 24px;
    letter-spacing: 0.3px;
    line-height: 1.1;
  }
  .holder-role {
    font-weight: 400;
    font-size: 14px;
    color: var(--muted);
    margin-top: 4px;
  }
  .divider {
    position: absolute;
    left: 222px;
    top: 170px;
    width: 1px;
    height: 80px;
    background: var(--rule);
  }
  .contacts {
    position: absolute;
    left: 240px;
    top: 174px;
    list-style: none;
  }
  .contacts li {
    display: flex;
    align-items: center;
    gap: 10px;
    font-size: 15px;
    font-weight: 400;
    height: 25px;
  }
  .contact-icon {
    width: 18px; height: 18px;
    background: var(--ink);
    display: flex; align-items: center; justify-content: center;
    flex: none;
  }
  .contact-icon svg { width: 12px; height: 12px; }
  /* Back */
  .card-back {
    left: 625px;
    background: var(--brand-blue);
    color: var(--paper);
  }
  .motto {
    position: absolute;
    font-weight: 300;
    font-size: 26px;
    letter-spacing: 1.5px;
  }
  .motto-create { left: 140px; top: 92px; }
  .motto-inspire { left: 360px; top: 158px; }
  .motto-tomorrow { left: 195px; top: 190px; }
  .back-mark {
    position: absolute;
    left: 248px; top: 110px;
    display: flex; flex-direction: column; align-items: center; gap: 6px;
  }
  .back-mark-dot {
    width: 36px; height: 36px;
    border-radius: 50%;
    background: var(--paper);
  }
  .back-mark-name {
    font-weight: 700;
    font-size: 11px;
    letter-spacing: 2px;
  }
</style>
</head>
<body>
  <section class="card card-front" aria-label="Business card front">
    <div class="brand">
      <span class="brand-dot" aria-hidden="true"></span>
      <span class="brand-name">BRONSALK MEDIA</span>
    </div>

    <div class="holder">
      <p class="holder-name">Paul Ardley</p>
      <p class="holder-role">Director Operations</p>
    </div>

    <span class="divider" aria-hidden="true"></span>

    <ul class="contacts">
      <li>
        <span class="contact-icon" aria-hidden="true">
          <svg viewBox="0 0 12 12"><rect x="3" y="1" width="6" height="10" rx="1" fill="none" stroke="#fff" stroke-width="1.3"/><circle cx="6" cy="9" r="0.7" fill="#fff"/></svg>
        </span>
        +61 452 118 906
      </li>
      <li>
        <span class="contact-icon" aria-hidden="true">
          <svg viewBox="0 0 12 12"><rect x="1" y="3" width="10" height="7" fill="none" stroke="#fff" stroke-width="1.2"/><path d="M1 3 L6 7 L11 3" fill="none" stroke="#fff" stroke-width="1.2"/></svg>
        </span>
        paulardley@bronsalk.com
      </li>
      <li>
        <span class="contact-icon" aria-hidden="true">
          <svg viewBox="0 0 12 12"><circle cx="6" cy="6" r="4.8" fill="none" stroke="#fff" stroke-width="1.1"/><ellipse cx="6" cy="6" rx="2" ry="4.8" fill="none" stroke="#fff" stroke-width="1"/><path d="M1.2 6 H10.8" stroke="#fff" stroke-width="1"/></svg>
        </span>
        www.bronsalk.com
      </li>
    </ul>
  </section>

  <section class="card card-back" aria-label="Business card back">
    <span class="motto motto-create">Create</span>
    <div class="back-mark">
      <span class="back-mark-dot" aria-hidden="true"></span>
      <span class="back-mark-name">BRONSALK</span>
    </div>
    <span class="motto motto-inspire">Inspire</span>
    <span class="motto motto-tomorrow">Tomorrow</span>
  </section>
</body>
</html>
```